Law firm Seeks Modern and Engaging Site Redesign

Law firm seeks a new web site. Should be modern, but retaining existing logo. Needs to include contact section, professional bio, services offered, and contact information.

The site should be modern, responsive, and able to be SEO optimized.

The finished product should be coded in a Wordpress site, which I will provide. I can work with other platforms, including Wix, but WP is preferred.

Note the current site is https://www.tallowfieldlaw.example/#/home

Target Market(s)

Family Law Practice

Industry/Entity Type

Legal

Coding

Coded - Design and coding required

Number of Pages Required

4 page

Font styles to use
Sans Serif

Requirements
Must have
• Service description
Bio pages for partners
Contact Form
Awards/Publication page

```html
<!DOCTYPE html>
<html lang="en">
<head>
<meta charset="utf-8">
<title>Tallow Field – Attorneys at Law</title>
<link href="https://fonts.googleapis.com/css2?family=Fira+Sans:wght@400;500;600;700&family=Lato:wght@400;700&display=swap" rel="stylesheet">
<style>
:root{
  --blue:#5673dc;
  --blue-light:#8fa7ef;
  --blue-band:#4f66c4;
  --ink:#333844;
  --text:#5a5f6b;
  --panel:#666666;
  --soft:#f3f3f5;
  --footer:#1e1e20;
  --white:#ffffff;
}
*{margin:0;padding:0;box-sizing:border-box}
html,body{width:1200px;height:3659px;overflow:hidden}
body{position:relative;font-family:'Lato',sans-serif;color:var(--text);background:var(--white)}
.abs{position:absolute}
.wordmark{display:flex;align-items:center;gap:10px;font-family:'Fira Sans',sans-serif;font-weight:400;font-size:26px;line-height:1;white-space:nowrap}
.wordmark .dot{width:12px;height:12px;background:currentColor}
.btn{position:absolute;display:flex;align-items:center;justify-content:center;gap:10px;border-radius:22px;font-family:'Fira Sans',sans-serif;font-weight:600;color:#fff;background:var(--blue-light)}
/* header */
.site-header{top:0;left:0;width:1200px;height:73px;background:#fff}
.nav{left:393px;top:28px;display:flex;font-family:'Fira Sans',sans-serif;font-size:14px;color:#666}
.nav a{display:block;padding:0 18px 14px;text-decoration:none;color:#666}
.nav a.active{color:var(--blue);border-bottom:1px solid var(--blue)}
.call{left:858px;top:12px;font-size:14px;color:#555}
.call strong{display:block;font-family:'Fira Sans',sans-serif;font-size:25px;color:var(--blue);font-weight:600;margin-top:2px;padding-left:27px}
/* hero */
.hero{top:73px;left:0;width:1200px;height:567px;background:linear-gradient(90deg,#8a8a8a,#6f6f72 50%,#6c7cc0 50%,#7788c9)}
.hero-left{left:10px;top:10px;width:590px;height:547px;background:linear-gradient(180deg,#8c8c8e,#77777a)}
.hero-right{left:600px;top:10px;width:590px;height:547px;background:linear-gradient(180deg,#6a7fd0,#5c6fc0)}
.hero h1{position:absolute;top:178px;font-family:'Fira Sans',sans-serif;font-weight:700;font-size:42px;color:#fff;letter-spacing:1px}
.hero .divider{left:598px;top:165px;width:4px;height:86px;background:#fff}
.hero .tag{position:absolute;top:290px;font-family:'Fira Sans',sans-serif;font-size:28px}
/* about */
.about-back{left:67px;top:720px;width:398px;height:450px;background:var(--blue-light)}
.about-img{left:102px;top:693px;width:398px;height:450px;background:radial-gradient(circle at 45% 45%,#8a5a2e,#2b1a10 60%,#101418)}
.accent{position:absolute;width:6px;background:var(--blue)}
.eyebrow{font-size:14px;color:#555}
.h2{font-family:'Fira Sans',sans-serif;font-weight:500;font-size:29px;color:var(--blue)}
.about-text{left:535px;top:720px;width:570px}
.about-text p{font-size:13.5px;line-height:24px;margin-top:14px}
/* practice */
.practice{top:1197px;left:0;width:1200px;height:382px;background:linear-gradient(180deg,#5a70c8,#4d64bf)}
.practice .eye{color:var(--blue-light);font-size:15px}
.practice h2{font-family:'Fira Sans',sans-serif;font-weight:500;color:#fff;font-size:29px}
.areas{left:0;top:130px;width:1200px}
.area{position:absolute;width:332px;text-align:center;font-family:'Fira Sans',sans-serif;font-size:24px;color:#b5c4f7}
.sep{position:absolute;width:3px;height:34px;background:#fff}
.stem{left:599px;width:3px;background:var(--blue)}
/* team */
.team{top:1579px;left:0;width:1200px;height:1020px;background:var(--soft)}
.card{position:absolute;width:529px;background:#fff}
.photo{position:absolute;left:0;top:0;width:272px;height:100%}
.badge{position:absolute;left:10px;bottom:10px;width:104px;height:46px;background:#fff;border-bottom:12px solid #f08a1c}
.card .body{position:absolute;left:291px;top:14px;width:225px}
.card h3{font-family:'Fira Sans',sans-serif;font-weight:600;font-size:19px;color:#3c3c44;line-height:23px}
.card p{font-size:13.2px;line-height:24px;margin-top:14px}
.card .btn{position:static;display:inline-flex;background:var(--blue);font-size:12px;height:29px;padding:0 10px;margin-top:14px}
/* contact */
.contact-back{left:57px;top:2680px;width:406px;height:470px;background:var(--blue-light)}
.contact-card{left:93px;top:2644px;width:406px;height:470px;background:var(--panel);color:#fff;text-align:center}
.contact-card .line{font-size:15px;line-height:26px}
.contact-card .big{font-size:21px}
.form{left:535px;top:2660px;width:573px}
.form .intro{font-size:13px;line-height:24px;color:#555;margin-top:16px;text-transform:uppercase}
.field{position:absolute;border-bottom:1px solid #d5d5d5;font-size:13px;color:#999;padding:0 14px 10px}
.send{position:absolute;left:0;width:573px;height:33px;background:var(--blue);color:#fff;font-family:'Fira Sans',sans-serif;font-weight:600;font-size:12px;display:flex;align-items:center;justify-content:center}
/* map & footer */
.map{top:3170px;left:0;width:1200px;height:301px;background:linear-gradient(135deg,#eef0ea,#e3e8e2 40%,#cfdcea 75%,#e9ece6)}
.footer{top:3471px;left:0;width:1200px;height:188px;background:var(--footer)}
.footer .copy{position:absolute;top:126px;width:1200px;text-align:center;color:#fff;font-size:13px}
</style>
</head>
<body>

<header class="site-header abs">
  <div class="wordmark abs" style="left:117px;top:23px;color:#6b6b6b"><span class="dot"></span>Tallow Field</div>
  <nav class="nav abs">
    <a class="active">Home</a><a>About</a><a>Services</a><a>Awards</a><a>Contact</a>
  </nav>
  <div class="call abs">call today for your free consultation<strong>(555) 310-2741</strong></div>
</header>

<section class="hero abs">
  <div class="hero-left abs" role="img" aria-label="Portrait of the criminal law partner in a suit"></div>
  <div class="hero-right abs" role="img" aria-label="Portrait of the family law partner in a suit"></div>
  <h1 style="left:229px">CRIMINAL LAW</h1>
  <div class="divider abs"></div>
  <h1 style="left:654px">FAMILY LAW</h1>
  <div class="tag" style="left:333px;color:#9fb3f5">Dont Feel HelpLess</div>
  <div class="tag" style="left:618px;color:#fff">We Fight For Justice</div>
  <div class="btn" style="left:442px;top:339px;width:140px;height:41px;font-size:13px">About Us</div>
  <div class="btn" style="left:618px;top:339px;width:132px;height:41px;font-size:13px;background:#fff;color:#333">Practice Area</div>
</section>

<div class="about-back abs"></div>
<div class="about-img abs" role="img" aria-label="Bronze scales of justice"></div>
<div class="accent" style="left:497px;top:712px;height:70px"></div>
<div class="about-text abs">
  <div class="eyebrow">About Tallow Field LLC</div>
  <div class="h2">Who We Are</div>
  <p>The law firm of Tallow Field, LLC is based in Alder County, conveniently located in Millbrook, New Jersey in 14 Harbor Court. We serve the needs of clients throughout Alder County, as well as, clients from several other counties, including, but not limited to, Ashford, Morrow, Easton and Halden. Between our partners, we have over 30+ years of experience assisting clients with all of their family law and criminal law needs.</p>
  <p>Often times the areas of family law and criminal law cross paths, which can be both emotionally and financially complex. We understand that our client’s case is unique and pride ourselves on being responsive to all of our clients needs.</p>
  <p>Whether your needs are family or criminal law related, contact Tallow Field, LLC to schedule a consultation.</p>
</div>
<div class="btn" style="left:535px;top:1103px;width:153px;height:40px;font-size:13px">Read more
  <svg width="14" height="10" viewBox="0 0 14 10"><path d="M0 5h12M8 1l4 4-4 4" stroke="#fff" stroke-width="2" fill="none"/></svg></div>

<section class="practice abs" role="img" aria-label="Blue band over courthouse columns">
  <div class="abs eye" style="top:42px;width:1200px;text-align:center">Practice Area</div>
  <h2 class="abs" style="top:62px;width:1200px;text-align:center">What We Cover</h2>
  <div class="areas abs">
    <div class="area" style="left:102px;top:12px">Criminal Law</div>
    <div class="area" style="left:434px;top:12px">Family Law</div>
    <div class="area" style="left:766px;top:12px">Municipal Court</div>
    <div class="area" style="left:102px;top:82px">Real Estate Law</div>
    <div class="area" style="left:434px;top:82px">Juvenile Practice</div>
    <div class="area" style="left:766px;top:82px">Wills / Trusts</div>
    <div class="sep" style="left:432px;top:11px"></div><div class="sep" style="left:765px;top:11px"></div>
    <div class="sep" style="left:432px;top:81px"></div><div class="sep" style="left:765px;top:81px"></div>
  </div>
  <div class="btn" style="left:525px;top:298px;width:150px;height:40px;font-size:13px">Read more
    <svg width="14" height="10" viewBox="0 0 14 10"><path d="M0 5h12M8 1l4 4-4 4" stroke="#fff" stroke-width="2" fill="none"/></svg></div>
</section>

<section class="team abs">
  <div class="stem abs" style="top:0;height:52px"></div>
  <div class="abs eyebrow" style="top:55px;width:1200px;text-align:center">Our Expert Team</div>
  <div class="abs h2" style="top:72px;width:1200px;text-align:center">Meet Our Attorneys</div>

  <article class="card" style="left:53px;top:175px;height:386px">
    <div class="photo" role="img" aria-label="Portrait of Martin R. Tallow in an office" style="background:linear-gradient(160deg,#c9c2b4,#6e6a66 60%,#3a2a24)"><div class="badge"></div></div>
    <div class="accent" style="left:271px;top:10px;height:28px"></div>
    <div class="body"><h3>Martin R. Tallow, Esq.</h3>
      <p>Martin R. Tallow practices in the area of family law, specializing in high conflict matters relating to divorce, custody, equitable distribution, and complex financial issues. Additionally, Mr. Tallow specializes in DCPP (formerly known as DYFS)-related litigation and DCPP defense matters, as well as domestic violence proceedings.</p>
      <span class="btn">Read More</span></div>
  </article>

  <article class="card" style="left:618px;top:175px;height:386px">
    <div class="photo" role="img" aria-label="Portrait of Daniel P. Field at his desk" style="width:255px;background:linear-gradient(160deg,#b9b3a8,#5d5651 55%,#3b2722)"><div class="badge"></div></div>
    <div class="accent" style="left:252px;top:10px;height:28px"></div>
    <div class="body" style="left:273px;width:240px"><h3>Daniel P. Field, Esq.</h3>
      <p>Daniel P. Field is one of the founding partners of the firm. Mr. Field’s primary concentration is in the areas of matrimonial, family law, appellate work, juvenile delinquency, criminal, municipal court, residential real estate transactions and wills and estates.</p>
      <span class="btn">Read More</span></div>
  </article>

  <article class="card" style="left:53px;top:598px;height:350px">
    <div class="photo" role="img" aria-label="Portrait of Laura M. Hayes outdoors" style="background:linear-gradient(160deg,#a99a8e,#7d6a60 50%,#2e2a2c)"><div class="badge"></div></div>
    <div class="accent" style="left:271px;top:10px;height:28px"></div>
    <div class="body"><h3>Laura M. Hayes, Esq.</h3>
      <p>Laura Hayes has been an associate at Tallow Field since 2016. In private practice, Ms. Hayes focuses her practice on family and divorce law, which includes child custody, child and spousal support, equitable distribution.</p>
      <span class="btn">Read More</span></div>
  </article>

  <article class="card" style="left:618px;top:598px;height:350px">
    <div class="photo" role="img" aria-label="Blue-tinted scales of justice" style="width:255px;background:linear-gradient(160deg,#6d86dc,#5a74d6 60%,#4e69cf)"></div>
    <div class="accent" style="left:252px;top:10px;height:28px"></div>
    <div class="body" style="left:273px;width:245px"><h3>Rebecca N. Santorelli, Esq.</h3>
      <p>Rebecca N. Santorelli, Esq. (“Becca”) is a skilled and experienced litigator specializing in all facets of family and matrimonial law. Ms. Santorelli’s practice includes marital dissolution and non-dissolution proceedings, child custody and support matters…</p>
      <span class="btn">Read More</span></div>
  </article>
</section>

<div class="contact-back abs"></div>
<aside class="contact-card abs">
  <div class="wordmark" style="justify-content:center;margin-top:52px;color:#e2e2e2"><span class="dot"></span>Tallow Field</div>
  <svg style="margin-top:46px" width="26" height="32" viewBox="0 0 26 32"><path d="M13 30C5 20 2 15 2 11a11 11 0 0 1 22 0c0 4-3 9-11 19z" fill="none" stroke="#9fb3f5" stroke-width="2"/><circle cx="13" cy="11" r="4" fill="none" stroke="#9fb3f5" stroke-width="2"/></svg>
  <div class="line">Tallow &amp; Field LLC 14 Harbor Court Drive<br>Suite 210 Millbrook, NJ 07990</div>
  <svg style="margin-top:26px" width="32" height="32" viewBox="0 0 32 32"><path d="M7 3l6 6-3 4c2 4 5 7 9 9l4-3 6 6-4 4C14 28 4 18 3 7z" fill="none" stroke="#9fb3f5" stroke-width="2" stroke-linejoin="round"/></svg>
  <div class="line big" style="margin-top:4px">(555) 310-2741</div>
  <svg style="margin-top:26px" width="32" height="32" viewBox="0 0 32 32"><rect x="3" y="12" width="26" height="17" fill="none" stroke="#9fb3f5" stroke-width="2"/><rect x="10" y="3" width="14" height="12" fill="none" stroke="#9fb3f5" stroke-width="2"/><path d="M9 18h4M9 23h4M18 18h6M18 23h6" stroke="#9fb3f5" stroke-width="2"/></svg>
  <div class="line big" style="margin-top:4px">(555) 310-2790</div>
</aside>
<div class="accent" style="left:496px;top:2660px;height:66px"></div>

<section class="form abs">
  <div class="h2">Contact Us</div>
  <div class="intro">To discuss your matter with either Mr. Tallow or Mr. Field send us your details about your situation or contact us directly at (555) 310-2741.</div>
  <div class="field" style="left:0;top:152px;width:285px">First Name</div>
  <div class="field" style="left:291px;top:152px;width:282px">Last Name</div>
  <div class="field" style="left:0;top:203px;width:285px">Email</div>
  <div class="field" style="left:291px;top:203px;width:282px">Phone</div>
  <div class="field" style="left:0;top:254px;width:573px;color:#555;display:flex;justify-content:space-between">Please Choose...<svg width="9" height="6" viewBox="0 0 9 6"><path d="M0 0h9L4.5 6z" fill="#555"/></svg></div>
  <div class="field" style="left:0;top:300px;width:573px;height:100px">Message</div>
  <div class="send" style="top:418px">SEND</div>
</section>

<div class="stem abs" style="top:3137px;height:52px;z-index:2"></div>
<div class="map abs" role="img" aria-label="Street map showing the office location"></div>

<footer class="footer abs">
  <div class="wordmark abs" style="left:0;width:1200px;justify-content:center;top:46px;color:#d6d6d6"><span class="dot"></span>Tallow Field</div>
  <div class="copy">Copyright © 2020 Tallow &amp; Field, LLC. All rights reserved.</div>
</footer>

</body>
</html>
```